Flyer Design Project

We need a flyer design for our company based in Ontario, Canada called CrateLoop. We rent out plastic reusable moving boxes. Please visit Crateloop.ca to find out more information about our company. We are looking for a creative, clean, and fun flyer design. The flyers purpose is to share with others what services CrateLoop offers as well as how convient our service is while still being cheaper than cardboard boxes.

Industry/Entity Type

Plastic

```html
<!DOCTYPE html>
<html lang="en">
<head>
<meta charset="utf-8">
<title>CrateLoop – Reusable Moving Boxes</title>
<link href="https://fonts.googleapis.com/css2?family=Arimo:wght@700&family=Russo+One&display=swap" rel="stylesheet">
<style>
  :root{
    --orange:#ff8a00;
    --orange-deep:#f57c00;
    --yellow:#ffe600;
    --green:#7fb800;
    --lime:#9be22a;
    --lime-light:#c9ff5e;
    --ink:#1d1d1d;
    --white:#ffffff;
    --tick:#1fc01f;
    --frame:#e8a21c;
    --cross:#d42020;
    --cardboard:#c8915a;
    --money:#b8c4a8;
  }
  html,body{margin:0;padding:0;overflow:hidden;background:#fff;}
  .flyer{
    position:relative;width:927px;height:1200px;overflow:hidden;
    background:radial-gradient(circle at 560px 640px,var(--yellow) 0,#ffc400 260px,var(--orange) 560px,var(--orange-deep) 800px);
    font-family:"Arimo",Arial,sans-serif;color:var(--ink);
  }
  .bands{position:absolute;inset:0;}
  .brand{position:absolute;left:50px;top:44px;display:flex;align-items:center;gap:22px;}
  .brand-mark{width:40px;height:40px;background:var(--ink);border-radius:6px;}
  .brand-name{font-size:78px;font-weight:700;line-height:.92;letter-spacing:-1px;text-transform:uppercase;}
  .copy{position:absolute;margin:0;font-weight:700;line-height:1.3;}
  .bullet{position:absolute;width:54px;height:36px;border-radius:6px;background:linear-gradient(#b9f04a,var(--lime));}
  .line-1{left:58px;top:252px;font-size:24px;}
  .line-2{left:141px;top:284px;font-size:24px;}
  .line-3{left:143px;top:319px;font-size:19px;}
  .pack{left:145px;top:370px;font-size:38px;}
  .protect{left:55px;top:417px;font-size:23px;line-height:1.32;}
  .collect{left:131px;top:504px;font-size:23px;line-height:1.45;}
  .bubble{position:absolute;border-radius:50%;background:var(--white);box-shadow:0 0 0 16px var(--orange);overflow:hidden;}
  .bubble-top{left:540px;top:116px;width:350px;height:350px;}
  .bubble-bottom{left:548px;top:812px;width:350px;height:350px;}
  .art{position:absolute;}
  .art-cardboard{left:60px;top:55px;width:235px;height:235px;border-radius:10px;background:linear-gradient(160deg,#e6bd8c,var(--cardboard));}
  .cross{position:absolute;left:112px;top:110px;width:120px;height:120px;}
  .art-money{left:0;top:80px;width:350px;height:150px;background:linear-gradient(90deg,#e4e9dc,var(--money),#e4e9dc);}
  .word{position:absolute;left:0;width:100%;text-align:center;font-family:"Russo One",Arial,sans-serif;font-size:50px;color:var(--ink);}
  .word-less{top:14px;}
  .word-paid{top:240px;}
  .art-crate{left:42px;top:620px;width:488px;height:350px;border-radius:26px;background:linear-gradient(180deg,var(--lime-light) 0,#b6f23e 20%,var(--lime) 60%,#8fd622);}
  .crate-lid{position:absolute;left:0;top:0;width:100%;height:70px;border-radius:26px 26px 10px 10px;background:#d6ff7a;opacity:.7;}
  .crate-name{position:absolute;left:160px;top:150px;display:flex;align-items:center;gap:12px;font-size:42px;font-weight:700;line-height:.92;text-transform:uppercase;}
  .crate-name span.dot{width:22px;height:22px;background:var(--ink);border-radius:4px;}
  .tick{position:absolute;left:458px;top:694px;width:140px;height:140px;}
  .arrow{position:absolute;}
  .phone{position:absolute;left:46px;top:1074px;font-family:"Russo One",Arial,sans-serif;font-size:45px;color:var(--ink);letter-spacing:1px;}
  .web{position:absolute;left:48px;top:1134px;font-size:26px;font-weight:700;color:var(--ink);}
</style>
</head>
<body>
<main class="flyer">
  <svg class="bands" width="927" height="1200" viewBox="0 0 927 1200" aria-hidden="true">
    <path d="M566 0 H710 C830 160 900 420 900 640 C900 900 760 1120 560 1200 H430 C640 1100 770 880 770 640 C770 400 700 180 566 0 Z" fill="var(--green)"/>
    <path d="M927 240 V1200 H340 C640 1140 860 900 880 640 C890 480 875 360 860 250 Z" fill="var(--ink)"/>
    <path d="M880 640 C870 900 680 1130 430 1200 H560 C760 1120 890 900 900 640 C900 500 890 380 860 250 C875 380 885 500 880 640 Z" fill="var(--green)"/>
  </svg>

  <header class="brand">
    <div class="brand-mark"></div>
    <div class="brand-name">Crate<br>Loop</div>
  </header>

  <p class="copy line-1">We deliver your moving boxes</p>
  <div class="bullet" style="left:66px;top:296px" role="img" aria-label="Small green plastic moving box"></div>
  <p class="copy line-2">right to your front door</p>
  <p class="copy line-3">(unless you prefer side door).</p>

  <div class="bullet" style="left:66px;top:374px" role="img" aria-label="Small green plastic moving box"></div>
  <p class="copy pack">Pack it up!</p>
  <p class="copy protect">Our boxes protect your belongings<br>and make stacking safe.</p>

  <div class="bullet" style="left:66px;top:510px" role="img" aria-label="Small green plastic moving box"></div>
  <p class="copy collect">Once you're unpacked<br>we'll come by your new home<br>and collect the moving boxes.</p>

  <div class="bubble bubble-top">
    <div class="art art-cardboard" role="img" aria-label="Open cardboard moving box"></div>
    <svg class="cross" viewBox="0 0 120 120" aria-hidden="true">
      <rect x="6" y="6" width="108" height="108" fill="none" stroke="var(--frame)" stroke-width="10"/>
      <path d="M22 22 L98 98 M98 22 L22 98" stroke="var(--cross)" stroke-width="20" stroke-linecap="round"/>
    </svg>
  </div>

  <svg class="arrow" style="left:560px;top:500px" width="150" height="150" viewBox="0 0 150 150" aria-hidden="true">
    <path d="M140 14 L118 0 L40 92 L22 72 L6 144 L78 128 L58 110 Z" fill="var(--white)"/>
  </svg>

  <div class="art art-crate" role="img" aria-label="Green transparent plastic moving crate with lid">
    <div class="crate-lid"></div>
    <div class="crate-name"><span class="dot"></span><span>Crate<br>Loop</span></div>
  </div>

  <svg class="tick" viewBox="0 0 140 140" aria-hidden="true">
    <rect x="8" y="8" width="124" height="124" fill="none" stroke="var(--frame)" stroke-width="12"/>
    <path d="M18 66 L58 104 L134 14" fill="none" stroke="var(--tick)" stroke-width="24" stroke-linecap="round" stroke-linejoin="round"/>
  </svg>

  <svg class="arrow" style="left:385px;top:940px" width="125" height="90" viewBox="0 0 125 90" aria-hidden="true">
    <path d="M0 20 L70 30 L66 6 L124 52 L56 88 L62 62 L6 48 Z" fill="var(--white)"/>
  </svg>

  <div class="bubble bubble-bottom">
    <div class="word word-less">LESS</div>
    <div class="art art-money" role="img" aria-label="Crumpled dollar bill"></div>
    <div class="word word-paid">PAID</div>
  </div>

  <div class="phone">1-800-555-0147</div>
  <div class="web">Crateloop.ca</div>
</main>
</body>
</html>
```